Disease outbreak warning

I need a flyer that explains to hunters how to act as frontline responders to potential disease outbreaks in wildlife populations. In this case the disease is African Swine Fever. We need an at a glance style with plenty of colour and that’s very easy to read.

I HAVE ATTACHED SOME EXISTING FLYERS FROM OVERSEAS ETC THAT CONTAIN SOME OF THE RELEVANT INFO. THEY ARE TO BE USED AS A GUIDE ONLY.
Updates

Need to see some more options. We have some that can be developed successfully but we’d like to see some more options that will suit a national campaign.

Target Market(s)

Australian hunters encountering wild pigs. Typical age is from 18 to 32 but can be older. Male or female.

Colors

Designer to choose colors to be used in the design.

Requirements
Must have
• The KWOTL logo (supplied). It should be relatively small at the bottom of the page. Plus we need room for two or three other logos that can be overprinted on the project if required.
• Must have information for hunters as the main focus.
Nice to have
• A double sided flyer.
Should not have
• US spelling.

```html
<!DOCTYPE html>
<html lang="en-AU">
<head>
<meta charset="utf-8">
<title>African Swine Fever – Hunter Flyer</title>
<link href="https://fonts.googleapis.com/css2?family=Oswald:wght@700&family=Open+Sans:wght@400;600;700&display=swap" rel="stylesheet">
<style>
  :root{
    --navy:#0e2f66;
    --navy-deep:#061a3d;
    --gold:#b78d0e;
    --paper:#f5f1ea;
    --ink:#1c1c1c;
    --ink-navy:#10306a;
    --alert:#c1272d;
    --stage:#8a8a8a;
    --white:#ffffff;
  }
  *{box-sizing:border-box;margin:0;padding:0}
  html,body{width:1200px;height:865px;overflow:hidden}
  body{background:var(--stage);font-family:"Open Sans",Arial,sans-serif;position:relative}
  .page{position:absolute;top:79px;width:500px;height:706px;background:var(--paper);overflow:hidden;box-shadow:0 4px 14px rgba(0,0,0,.35)}
  .page--front{left:72px}
  .page--back{left:626px}
  .abs{position:absolute}

  /* front */
  .title{left:0;right:0;top:10px;text-align:center;font-family:"Oswald",Impact,sans-serif;font-weight:700;font-size:46px;line-height:56px;color:var(--gold);white-space:nowrap;transform:scaleY(1.15)}
  .strapline{left:0;right:0;top:66px;height:33px;background:var(--navy);color:var(--white);font-weight:700;font-size:14.5px;line-height:33px;text-align:center;white-space:nowrap}
  .hero{left:0;right:0;top:102px;height:220px;background:linear-gradient(160deg,#7a8a3c 0%,#3f4a22 40%,#2a2a22 70%,#6b7a88 100%)}
  .intro{left:0;right:0;top:326px;height:85px;background:linear-gradient(90deg,var(--navy),var(--navy-deep));color:var(--white);font-size:13px;line-height:18px;text-align:center;padding:11px 26px 0}
  .tab{background:var(--gold);color:var(--white);font-weight:700;border-radius:0 0 16px 0;white-space:nowrap}
  .tab--detect{left:0;top:411px;width:306px;height:43px;font-size:20px;line-height:43px;padding-left:19px}
  .signs-heading{left:17px;top:471px;width:300px;color:var(--ink-navy);font-weight:700;font-size:13px;line-height:18px}
  .signs-rule{left:17px;top:511px;width:66px;height:2px;background:var(--ink)}
  .checklist{list-style:none}
  .checklist li{position:relative;padding-left:18px;color:var(--ink);font-weight:600}
  .checklist svg{position:absolute;left:0;top:2px;width:12px;height:12px}
  .signs-a{left:19px;top:526px;width:210px;font-size:11px;line-height:15px}
  .signs-a li:nth-child(1){height:35px}
  .signs-a li:nth-child(2){height:23px}
  .signs-a li:nth-child(3){height:27px}
  .signs-b{left:228px;top:526px;width:92px;font-size:11px;line-height:15px}
  .signs-b li{height:27px}
  .carcass{left:319px;top:457px;width:166px;height:177px;background:var(--gold);color:var(--white);padding:9px 3px 0 10px}
  .carcass h3{font-size:12.5px;font-weight:700;line-height:17px;margin-bottom:4px;white-space:nowrap}
  .carcass-rule{width:58px;height:1px;background:var(--white);margin-bottom:6px}
  .carcass .checklist li{color:var(--white);font-weight:400;font-size:8.8px;line-height:11.5px;padding-left:15px;margin-bottom:7px}
  .carcass .checklist svg{width:10px;height:10px;top:1px}
  .foot{left:0;right:0;bottom:0;background:linear-gradient(90deg,var(--navy-deep),var(--navy));color:var(--white)}
  .foot--front{height:64px}
  .logo-slot{left:19px;top:8px;width:74px;height:44px;background:var(--white);color:var(--ink);font-size:18px;line-height:44px;text-align:center}
  .hotline{left:100px;top:9px;width:300px;text-align:center}
  .hotline-label{font-size:10.5px;line-height:14px;white-space:nowrap}
  .hotline-number{font-weight:700;font-size:24px;line-height:30px}
  .client-mark{right:14px;top:20px;display:flex;align-items:center;gap:5px;font-weight:700;font-size:13px}
  .client-mark i{display:block;width:22px;height:22px;border-radius:50%;background:var(--white)}

  /* back */
  .topbar{left:16px;width:467px;top:0;height:13px;background:var(--navy)}
  .tab--prevent{left:24px;top:41px;width:386px;height:35px;font-size:19px;line-height:35px;padding-left:31px;border-radius:0 0 14px 0}
  .tab--donot{left:24px;top:348px;width:189px;height:41px;font-size:26px;line-height:43px;padding-left:31px;border-radius:0 0 16px 0}
  .actions{left:50px;width:440px;list-style:none}
  .actions li{position:absolute;left:0;padding-left:28px;font-size:14px;line-height:18.5px;color:var(--ink);white-space:nowrap}
  .actions svg{position:absolute;left:0;top:1px;width:17px;height:17px}
  .actions--warn svg{color:var(--alert)}
  .foot--back{height:77px;font-size:10px;line-height:13px}
  .foot-col{top:18px}
  .foot-col--left{left:38px;width:205px}
  .foot-col--right{left:270px;width:222px;border-left:1px solid var(--white);padding-left:26px;top:20px;height:42px}
  .foot-col--right .foot-note{font-size:9px;line-height:12px}
  .foot-phone{display:flex;align-items:center;gap:4px;font-size:12px;font-weight:600;margin-top:4px}
  .foot-phone svg{width:11px;height:11px}
</style>
</head>
<body>
<svg width="0" height="0" style="position:absolute">
  <defs>
    <symbol id="tick" viewBox="0 0 20 20"><path d="M17 9.5A7.5 7.5 0 1 1 12.5 3" fill="none" stroke="currentColor" stroke-width="2"/><path d="M6 9.5l3.5 3.5L18 3.5" fill="none" stroke="currentColor" stroke-width="2.2"/></symbol>
    <symbol id="warn" viewBox="0 0 20 20"><path d="M10 2L18.5 17.5H1.5Z" fill="none" stroke="currentColor" stroke-width="1.8" stroke-linejoin="round"/><path d="M10 7.5v5" stroke="currentColor" stroke-width="1.8"/><circle cx="10" cy="14.8" r="1" fill="currentColor"/></symbol>
    <symbol id="phone" viewBox="0 0 20 20"><path d="M5 2l3 4-2 2c1 2.5 3.5 5 6 6l2-2 4 3-2 3C9 18 2 11 2 4Z" fill="currentColor"/></symbol>
  </defs>
</svg>

<section class="page page--front">
  <h1 class="abs title">AFRICAN SWINE FEVER</h1>
  <div class="abs strapline">HUNTERS ARE ON THE AUSTRALIAN BIOSECURITY FRONTLINE</div>
  <div class="abs hero" role="img" aria-label="Photograph of a feral boar with tusks lying in grass"></div>
  <p class="abs intro">African Swine Fever is on our doorstep and hunters should be on the lookout for any sign ASF has reached our shores. It has the potential to destroy Australia’s domestic pork industry and cause widespread hunting bans. It must be contained.</p>
  <div class="abs tab tab--detect">EARLY DETECTION IS VITAL.</div>
  <h2 class="abs signs-heading">The Signs Of African Swine Fever In Pigs Can Include:</h2>
  <div class="abs signs-rule"></div>
  <ul class="abs checklist signs-a">
    <li><svg><use href="#tick"/></svg>Death (possibly Before Other Signs Are Noticeable)</li>
    <li><svg><use href="#tick"/></svg>Blotching/reddening Of The Skin.</li>
    <li><svg><use href="#tick"/></svg>Lack Of Coordination Or Stiff Gait.</li>
    <li><svg><use href="#tick"/></svg>Difficulty Breathing.</li>
  </ul>
  <ul class="abs checklist signs-b">
    <li><svg><use href="#tick"/></svg>Diarrhoea.</li>
    <li><svg><use href="#tick"/></svg>Abortion.</li>
    <li><svg><use href="#tick"/></svg>Vomiting.</li>
    <li><svg><use href="#tick"/></svg>High Fever.</li>
  </ul>
  <div class="abs carcass">
    <h3>Inspect Carcasses For:</h3>
    <div class="carcass-rule"></div>
    <ul class="checklist">
      <li><svg><use href="#tick"/></svg>Pinpoint Reddening In Organs<br>Such As Heart And Kidneys.</li>
      <li><svg><use href="#tick"/></svg>Enlarged Lymph Nodes<br>Resembling Blood Clots.</li>
      <li><svg><use href="#tick"/></svg>Enlarged, Fragile And/or<br>Dark-coloured Spleen.</li>
      <li><svg><use href="#tick"/></svg>Excess Fluid Around The Heart.</li>
      <li><svg><use href="#tick"/></svg>Reddening Of The Skin.</li>
    </ul>
  </div>
  <footer class="abs foot foot--front">
    <div class="abs logo-slot">logos</div>
    <div class="abs hotline">
      <p class="hotline-label">If you suspect ASF, call the Emergency Animal Disease Hotline</p>
      <p class="hotline-number">1800 555 014</p>
    </div>
    <div class="abs client-mark"><i></i>KWOTL</div>
  </footer>
</section>

<section class="page page--back">
  <div class="abs topbar"></div>
  <h2 class="abs tab tab--prevent">To Prevent The Spread Of Disease:</h2>
  <ul class="abs actions" style="top:0">
    <li style="top:108px"><svg><use href="#tick"/></svg>Wear Disposable Or Washable Protective Clothing<br>(aprons / Gloves / Overalls) When Dressing Feral Pigs.</li>
    <li style="top:157px"><svg><use href="#tick"/></svg>Inspect All Carcasses And Carcass Parts For Evidence<br>Of Disease Or Illness.</li>
    <li style="top:204px"><svg><use href="#tick"/></svg>Respect All Quarantines, Biosecurity Plans And Restrictions<br>That Are In Place.</li>
    <li style="top:251px"><svg><use href="#tick"/></svg>Thoroughly Clean And Disinfect Vehicle After Each Hunt.</li>
    <li style="top:282px"><svg><use href="#tick"/></svg>Clean And Disinfect All Equipment On Site.</li>
    <li style="top:314px"><svg><use href="#tick"/></svg>Only Hunt On One Property Each Hunt.</li>
  </ul>
  <h2 class="abs tab tab--donot">DO NOT</h2>
  <ul class="abs actions actions--warn" style="top:0">
    <li style="top:425px"><svg><use href="#warn"/></svg>Have Contact With Domestic Pigs If You Hunt Feral Pigs.</li>
    <li style="top:457px"><svg><use href="#warn"/></svg>Move Live Animals (including Piglets) To New Locations</li>
    <li style="top:489px"><svg><use href="#warn"/></svg>Use Swill (meat And Food Scraps) To Feed Or Trap Feral Pigs</li>
    <li style="top:522px"><svg><use href="#warn"/></svg>Leave Leftovers From Your Meals In The Hunting Area.</li>
    <li style="top:554px"><svg><use href="#warn"/></svg>Feed Raw Feral Pork To Dogs</li>
    <li style="top:587px"><svg><use href="#warn"/></svg>keep feral pigs at home</li>
  </ul>
  <footer class="abs foot foot--back">
    <div class="abs foot-col foot-col--left">
      <p>If You Suspect Asf, Call The Emergency Animal Disease Hotline</p>
      <p class="foot-phone"><svg><use href="#phone"/></svg>1800 555 014</p>
    </div>
    <div class="abs foot-col foot-col--right">
      <p class="foot-note">The Kestrel Wild Outdoor Trackers League, A Part Of Australia’s Bio-security Network.</p>
      <p class="foot-phone"><svg><use href="#phone"/></svg>1300 555 927</p>
    </div>
  </footer>
</section>
</body>
</html>
```